Business Card Design Project

Business card incoporating newly designed logo. The business cards will be magnets and I would like the same design as previously provided (Blue colour swatch with logo up the top) Please note that the logo incorporates a website so it needs to be legible.
The blue colours in teh swatch ideally will be in the same range as the blue of the logo.
The copy should all be in the same colour ie. black if in the white lines or white if in the swatch itself
Updates

Hi All

Some of the designs are very close to what I am after.  I have added logo and updated brief to assist with design.  This project is not refundable so I will be selecting a design.

Hi All

We are looking for a business card as per the brief (colour swatch style) as mentioned it is also a magnet so it needs to be created to the specs supplied.  Being a magnet there is also no requirment for reverse design.

Cheers
Marcy

Industry/Entity Type

Business

Requirements
Must have
• Blue colour swatch design. (see attached current example)
KW Coatings logo (colour) up the top
I require 1 design but 2 versions (with two peoples names and mobile numbers)

The magnets will be printed by PrintHollow.com.au And you can find the full specs online http://www.printhollow.com.au/custom-magnets.aspx

```html
<!DOCTYPE html>
<html lang="en">
<head>
<meta charset="utf-8">
<title>KW Coatings – Business Card Magnet</title>
<link rel="stylesheet" href="https://fonts.googleapis.com/css2?family=Arimo:wght@400;700&display=swap">
<style>
  :root {
    --paper: #ffffff;
    --brand-blue: #1a74bb;
    --swatch-1: #063f7c;
    --swatch-2: #0d5aa0;
    --swatch-3: #1b7cc4;
    --swatch-4: #2a9ad8;
    --swatch-5: #40b9fb;
    --ink-light: #ffffff;
    --crop: #222222;
  }
  html, body {
    margin: 0;
    padding: 0;
    overflow: hidden;
    background: var(--paper);
  }
  .card {
    position: relative;
    width: 695px;
    height: 1200px;
    background: var(--paper);
    overflow: hidden;
    font-family: "Arimo", Arial, sans-serif;
  }
  .brand {
    position: absolute;
    top: 0;
    left: 0;
    width: 695px;
    height: 283px;
    display: flex;
    align-items: center;
    justify-content: center;
  }
  .brand-name {
    margin: 0;
    font-size: 92px;
    font-weight: 700;
    color: var(--brand-blue);
    letter-spacing: -1px;
    line-height: 1;
  }
  .swatch {
    position: absolute;
    left: 0;
    width: 695px;
    height: 164px;
    box-sizing: border-box;
    padding: 0 0 20px 48px;
    display: flex;
    align-items: flex-end;
    color: var(--ink-light);
    font-size: 38px;
    font-weight: 400;
    line-height: 1;
  }
  .swatch--name    { top: 283px; background: var(--swatch-1); }
  .swatch--phone   { top: 461px; background: var(--swatch-2); }
  .swatch--web     { top: 636px; background: var(--swatch-3); }
  .swatch--email   { top: 813px; background: var(--swatch-4); }
  .swatch--tagline { top: 988px; background: var(--swatch-5); padding-left: 0; justify-content: center; }
  .crop {
    position: absolute;
    background: var(--crop);
  }
  .crop--v { width: 1px; height: 14px; }
  .crop--h { width: 14px; height: 1px; }
</style>
</head>
<body>
  <main class="card">
    <header class="brand">
      <h1 class="brand-name">KW Coatings</h1>
    </header>

    <div class="swatch swatch--name">Glen Harrow</div>
    <div class="swatch swatch--phone">0400 555 019</div>
    <div class="swatch swatch--web">kwcoatings.com.au</div>
    <div class="swatch swatch--email">info@kwcoatings.com.au</div>
    <div class="swatch swatch--tagline">All Commercial &amp; Domestic Painting</div>

    <span class="crop crop--v" style="left:22px; top:0;"></span>
    <span class="crop crop--v" style="right:22px; top:0;"></span>
    <span class="crop crop--h" style="left:0; top:22px;"></span>
    <span class="crop crop--h" style="right:0; top:22px;"></span>
    <span class="crop crop--v" style="left:22px; bottom:0;"></span>
    <span class="crop crop--v" style="right:22px; bottom:0;"></span>
    <span class="crop crop--h" style="left:0; bottom:22px;"></span>
    <span class="crop crop--h" style="right:0; bottom:22px;"></span>
  </main>
</body>
</html>
```